TR Stationery - Modern Contemporary

Develop modern template for Letterhead and Stationery (business card, letterhead, envelopes) using the TR Logo and Icon

Colors
0054AA
0677BA
7BADD7
CADEEF
E8F1F8
00AB8E
00BBA5
67D7C9
C6EFE9
E9F9F6
EE7325
F08F49
F5BC92
FAE3D3
FDF4ED
6B429C
8869AF
B7A5CE
E3DAEB
F3F0F8

```html
<!DOCTYPE html>
<html lang="en">
<head>
<meta charset="utf-8">
<title>Letterhead – terra rovi</title>
<link rel="stylesheet" href="https://fonts.googleapis.com/css2?family=Urbanist:wght@400;600&family=Libre+Baskerville&display=swap">
<style>
  :root {
    --green: #1fc278;
    --orange: #ff8a30;
    --navy: #262a44;
    --navy-deep: #2b2f4b;
    --ink-dark: #161c24;
    --text: #34374e;
    --paper: #fdfdfe;
    --sig-tone: #eeeff3;
  }
  * { margin: 0; padding: 0; box-sizing: border-box; }
  html, body { width: 849px; height: 1200px; overflow: hidden; background: #ffffff; }
  .letterhead {
    position: relative; width: 849px; height: 1200px; overflow: hidden;
    background: var(--paper);
    font-family: "Urbanist", sans-serif; color: var(--text);
    font-size: 17.8px; line-height: 19.9px;
  }
  .top-band { position: absolute; top: 0; left: 0; width: 100%; height: 10px; display: flex; }
  .top-band span:first-child { flex: 1; background: var(--green); }
  .top-band span:last-child { flex: 1; background: var(--orange); }

  .brand {
    position: absolute; left: 75px; top: 64px;
    font-family: "Urbanist", sans-serif; font-weight: 600; font-size: 40px; line-height: 48px;
    color: var(--navy); letter-spacing: 0.5px;
  }

  .salutation { position: absolute; left: 75px; top: 243px; }
  .letter-body { position: absolute; left: 75px; top: 285px; width: 706px; }
  .letter-body p + p { margin-top: 19.9px; }

  .signoff { position: absolute; left: 75px; top: 838px; }
  .signature { position: absolute; left: 72px; top: 884px; width: 130px; height: 48px; background: var(--sig-tone); border-radius: 4px; }
  .signoff-title { position: absolute; left: 75px; top: 938px; }

  .footer-mark { position: absolute; left: 0; top: 1087px; width: 69px; height: 37px; display: flex; }
  .footer-mark span:first-child { width: 64px; background: var(--green); }
  .footer-mark span:last-child { width: 5px; background: var(--orange); }
  .footer-name {
    position: absolute; left: 75px; top: 1084px;
    font-family: "Libre Baskerville", serif; font-size: 23px; line-height: 1;
    color: var(--navy); letter-spacing: -0.3px;
  }
  .footer-role { position: absolute; left: 75px; top: 1109px; font-size: 17px; line-height: 1; color: var(--navy); }
  .footer-address {
    position: absolute; left: 629px; top: 1087px; height: 37px;
    border-left: 1px solid var(--navy); padding-left: 7px;
    font-size: 15px; line-height: 18px; color: var(--navy); font-style: normal;
  }

  .bottom-band { position: absolute; left: 0; bottom: 0; width: 100%; height: 32px; display: flex; }
  .bottom-band span:first-child { flex: 1; background: var(--navy-deep); }
  .bottom-band span:last-child { flex: 1; background: var(--ink-dark); }
</style>
</head>
<body>
<main class="letterhead">
  <div class="top-band"><span></span><span></span></div>

  <header class="brand">terra rovi</header>

  <p class="salutation">Dear Sir,</p>

  <section class="letter-body">
    <p>Lorem Ipsum is simply dummy text of the printing and typesetting industry. Lorem Ipsum has been the industry's standard dummy text ever since the 1500s, when an unknown printer took a galley of type and scrambled it to make a type specimen book. It has survived not only five centuries, but also the leap into electronic typesetting, remaining essentially unchanged. It was popularised in the 1960s with the release of Linotrace sheets containing Lorem Ipsum passages, and more recently with desktop publishing software like Folio PageSetter including versions of Lorem Ipsum.</p>
    <p>It is a long established fact that a reader will be distracted by the readable content of a page when looking at its layout. The point of using Lorem Ipsum is that it has a more-or-less normal distribution of letters, as opposed to using 'Content here, content here', making it look like readable English. Many desktop publishing packages and web page editors now use Lorem Ipsum as their default model text, and a search for 'lorem ipsum' will uncover many web sites still in their infancy. Various versions have evolved over the years, sometimes by accident, sometimes on purpose (injected humour and the like).</p>
    <p>Contrary to popular belief, Lorem Ipsum is not simply random text. It has roots in a piece of classical Latin literature from 45 BC, making it over 2000 years old. Robert Ashgrove, a Latin professor at Halford College in Virginia, looked up one of the more obscure Latin words, consectetur, from a Lorem Ipsum passage, and going through the cites of the word in classical literature, discovered the undoubtable source. Lorem Ipsum comes from sections 1.10.32 and 1.10.33 of "de Finibus Bonorum et Malorum" (The Extremes of Good and Evil) by Lucius Tarvo, written in 45 BC. This book is a treatise on the theory of ethics, very popular during the Renaissance. The first line of Lorem Ipsum, "Lorem ipsum dolor sit amet..", comes from a line in section 1.10.32.</p>
  </section>

  <p class="signoff">Sencerly<br>Talia Rennick</p>
  <div class="signature" role="img" aria-label="Handwritten signature"></div>
  <p class="signoff-title">Associate Director</p>

  <footer>
    <div class="footer-mark"><span></span><span></span></div>
    <p class="footer-name">TALIA RENNICK</p>
    <p class="footer-role">Associate Director</p>
    <address class="footer-address">42 Larkfield Row<br>Brightwell, BW4 7QT</address>
  </footer>

  <div class="bottom-band"><span></span><span></span></div>
</main>
</body>
</html>
```